Online-Marketing Material für Hundetraining
Zielgruppe
Hundetraining. Ich coache Hundehalter und unterstütze sie darin ihrem Hund Führung zu geben. Im Vordergrund steht die natürliche Kommunikation mit dem Hund - komplett ohne Leckerchen.
Aufgabenstellung
Ich brauche ein Design für eine Facebookwerbeanzeige. Der Titel meines Videokurses ist 'Ruhig voran im Alltag'. Inhaltlich geht es in dem Kurs darum, wie Hundehalter der akzeptierte Entscheidungsträger werden können, indem wir am Grundrespekt arbeiten und die eigene Führungskompetenzen ausbauen.

```html
<!DOCTYPE html>
<html lang="de">
<head>
<meta charset="utf-8">
<title>Ruhig voran im Alltag – Anzeige</title>
<link rel="stylesheet" href="https://fonts.googleapis.com/css2?family=Raleway:wght@500;800&family=Open+Sans:wght@700&family=Yellowtail&display=swap">
<style>
  :root {
    --stage: #7a7879;
    --teal: #07b2aa;
    --white: #ffffff;
    --orange: #de8b1e;
    --fur-light: #f2c98a;
    --fur-mid: #e0a55a;
    --fur-dark: #c4823a;
  }
  * { margin: 0; padding: 0; box-sizing: border-box; }
  html, body {
    width: 1200px; height: 864px; overflow: hidden;
    background: var(--stage);
  }
  .ad {
    position: absolute; left: 40px; top: 95px;
    width: 1120px; height: 674px;
    background: var(--teal);
    overflow: hidden;
  }
  .photo-dog {
    position: absolute; left: 9px; top: 52px;
    width: 542px; height: 622px;
    border-radius: 260px 260px 0 0;
    background: radial-gradient(ellipse at 50% 35%, var(--fur-light) 0%, var(--fur-mid) 60%, var(--fur-dark) 100%);
  }
  .brand {
    position: absolute; left: 661px; top: 36px; width: 302px;
    display: flex; flex-direction: column; align-items: center; gap: 14px;
  }
  .brand-mark {
    width: 86px; height: 86px; border-radius: 50%;
    background: var(--white);
  }
  .brand-name {
    font-family: "Open Sans", sans-serif; font-weight: 700;
    font-size: 16px; color: var(--white); letter-spacing: 0.3px;
  }
  .headline-box {
    position: absolute; background: var(--white);
    display: flex; align-items: center; justify-content: center;
    font-family: "Raleway", sans-serif; font-size: 45px;
    color: var(--teal); letter-spacing: 0.5px; white-space: nowrap;
  }
  .headline-box.bold { font-weight: 800; }
  .headline-box.light { font-weight: 500; }
  .line-1 { left: 588px; top: 190px; width: 441px; height: 73px; }
  .line-2 { left: 569px; top: 277px; width: 481px; height: 74px; }
  .line-3 { left: 561px; top: 367px; width: 498px; height: 74px; }
  .tagline {
    position: absolute; left: 556px; top: 470px; width: 510px;
    text-align: center; font-family: "Yellowtail", cursive;
    font-size: 46px; color: var(--white); white-space: nowrap;
  }
  .cta {
    position: absolute; left: 661px; top: 564px;
    width: 301px; height: 58px; border-radius: 29px;
    background: var(--orange);
    box-shadow: 0 6px 14px rgba(0,0,0,0.22);
    display: flex; align-items: center; justify-content: center;
    font-family: "Open Sans", sans-serif; font-weight: 700;
    font-size: 24px; color: var(--white); letter-spacing: 0.3px;
  }
</style>
</head>
<body>
  <main class="ad">
    <div class="photo-dog" role="img" aria-label="Foto eines freundlichen Golden Retrievers mit heraushängender Zunge"></div>

    <div class="brand">
      <div class="brand-mark"></div>
      <div class="brand-name">RUDELWEG.DE</div>
    </div>

    <div class="headline-box bold line-1">MEIN BESITZER</div>
    <div class="headline-box bold line-2">TRAINIERT MICH</div>
    <div class="headline-box light line-3">OHNE LECKERLIS</div>

    <p class="tagline">und es funktioniert gut!</p>

    <div class="cta">INTERESSIERT?</div>
  </main>
</body>
</html>
```